I already have a logo created by Quillory Makers that I'm very happy with. I need to spruce up my business card now. Its a double sided card with not much info on it, I like to keep it simple.
Front of card: name, phone # email address, web address. Tag Line "Outsourced Technology Solutions", under that it says Business Voice Services & Electronic Protection.
Rear of Card: Content written inside a "cloud" saying "Cloud Solutions" "Cloud Integrity"

Target Market(s)

Business to Business

Industry/Entity Type

Business

Contact Information for Business Card

We are in the technology field. Providing Telephone systems (hardware), SIP Trunks (dial tone/local/long distance/telephone #'s), LAN (Local Area Network)infrastructure cabling, Data Center solutions and Security Applications (Camera systems, Access Control systems,

Requirements
Must have
• Must have brevity
Should not have
• Clutter and/or too much information

```html
<!DOCTYPE html>
<html lang="en">
<head>
<meta charset="utf-8">
<title>Northvale Signal — Business Card</title>
<link rel="stylesheet" href="https://fonts.googleapis.com/css2?family=Raleway:wght@300;400;700&family=Source+Sans+3:wght@400&display=swap">
<style>
  :root {
    --navy: #1b4180;
    --grey-text: #6f6f6f;
    --rule: #9a9a9a;
    --paper: #ffffff;
    --backdrop: #e4e5e7;
    --cloud-text: #7a7a7a;
  }
  * { box-sizing: border-box; margin: 0; padding: 0; }
  html, body { width: 1200px; height: 1200px; overflow: hidden; }
  body { background: var(--backdrop); position: relative; font-family: "Source Sans 3", sans-serif; }

  .card {
    position: absolute; left: 262px; width: 675px; height: 382px;
    box-shadow: 0 4px 12px rgba(0,0,0,0.18);
  }
  .card--front { top: 194px; background: var(--paper); }
  .card--back { top: 622px; background: var(--navy); overflow: hidden; }

  .brand-block {
    position: absolute; left: 300px; width: 354px; top: 36px;
    text-align: center;
  }
  .brand-name {
    display: inline-flex; align-items: center; gap: 10px;
    font-family: "Raleway", sans-serif; font-weight: 700; font-size: 27px;
    color: var(--navy); letter-spacing: 0.2px; line-height: 1;
    height: 70px;
  }
  .brand-mark { width: 16px; height: 16px; background: var(--navy); }
  .brand-rule { width: 282px; height: 2px; background: var(--rule); margin: 6px auto 0; }
  .tagline {
    font-family: "Raleway", sans-serif; font-weight: 400; font-size: 19px;
    color: var(--grey-text); margin-top: 4px;
  }
  .services {
    font-family: "Raleway", sans-serif; font-weight: 400; font-size: 13.5px;
    color: var(--navy); margin-top: 12px;
  }

  .name-bar { position: absolute; left: 0; top: 217px; width: 13px; height: 43px; background: var(--navy); }
  .person { position: absolute; left: 34px; top: 210px; }
  .person-name { font-size: 26px; color: var(--navy); line-height: 1.1; }
  .person-role { font-size: 17px; color: var(--grey-text); margin-top: 2px; }
  .contact { position: absolute; left: 34px; top: 281px; font-size: 17px; color: var(--grey-text); line-height: 23px; }

  .back-web { position: absolute; left: 34px; top: 335px; font-size: 17px; color: var(--paper); }
  .cloud { position: absolute; left: 0; top: 0; }
  .cloud-text {
    position: absolute; left: 415px; width: 200px; top: 282px;
    font-family: "Raleway", sans-serif; font-weight: 300; font-size: 27px;
    color: var(--cloud-text); text-align: center; line-height: 33px;
  }
</style>
</head>
<body>
  <section class="card card--front">
    <div class="brand-block">
      <div class="brand-name"><span class="brand-mark"></span>Northvale Signal, LLC</div>
      <div class="brand-rule"></div>
      <p class="tagline">Outsourced Technology Solutions</p>
      <p class="services">Business Voice Services &amp; Electronic Protection</p>
    </div>
    <div class="name-bar"></div>
    <div class="person">
      <p class="person-name">Marcus Hale</p>
      <p class="person-role">managing partner</p>
    </div>
    <div class="contact">
      <p>555-0142</p>
      <p>mhale@northvalesignal.com</p>
      <p>www.northvalesignal.com</p>
    </div>
  </section>

  <section class="card card--back">
    <svg class="cloud" width="675" height="382" viewBox="0 0 675 382">
      <g fill="#ffffff">
        <circle cx="426" cy="322" r="74"/>
        <circle cx="538" cy="290" r="86"/>
        <circle cx="689" cy="346" r="80"/>
        <rect x="426" y="310" width="249" height="72"/>
      </g>
    </svg>
    <p class="back-web">www.northvalesignal.com</p>
    <div class="cloud-text">
      <p>Cloud Solutions</p>
      <p>Cloud Integrity</p>
    </div>
  </section>
</body>
</html>
```